Corporate Capability Brochure for LumoByte

Create Corporate Capability Brochure for Executive IT Consulting Firm. Minority Business Enterprise (MBE) and Service Disabled Veteran Owned Small Business (SDVOSB). LumoByte is an Executive Information Technology Consulting Firm. We specialize in combining people with technology to deliver the Business of IT. We partner with C-Level Executives and their organizations to leverage technology that drives innovation and accelerates business transformation and enable businesses, governments and educational institutions to operate more successfully in a world where everything is increasingly linked together.

Looking for something clean, professional, innovative, eye-catching and creates a strong presence. The final design should communicate our numerous service offerings.

We are in the processing of updating our website so please use information obtained from capability statement uploaded. PLEASE USE LUMOBYTE CAPABILITY STATEMENT-COMMERCIAL (FILE 1) for content to be used in flyer/brochure being requested. Presentation was uploaded as a document to gauge style. We are still in the process of finding our style when it comes to marketing materials. Creativity is highly welcomed.

Target Market(s)

C-Level Executives. We work with Education Institutions, Healthcare Agencies, Federal Government Clients, Sports and Entertainment Companies and Technology companies.

Industry/Entity Type

Information Technology

Requirements
Should not have
• No Dark Backgrounds that make it hard to see
• No playful fonts that come across unprofessional
• Would prefer not to have images of people-Unless image provides Diversity

```html
<!DOCTYPE html>
<html lang="en">
<head>
<meta charset="utf-8">
<title>LumoByte Capability Brochure</title>
<link rel="stylesheet" href="https://fonts.googleapis.com/css2?family=Cinzel:wght@400;600&family=Lato:wght@400;700&display=swap">
<style>
:root{
  --red:#d01c29;
  --red-dark:#a8141e;
  --grey:#5d5d5f;
  --grey-light:#dcdcdc;
  --ink:#3a3a3a;
  --paper:#ffffff;
  --backdrop:#ecebe8;
}
*{box-sizing:border-box;margin:0;padding:0}
html,body{width:1200px;height:1200px;overflow:hidden}
body{background:var(--backdrop);font-family:'Lato',sans-serif;color:var(--ink);position:relative}
.page{position:absolute;top:200px;width:556px;height:780px;background:var(--paper);box-shadow:0 4px 14px rgba(0,0,0,.25);overflow:hidden}
.page--front{left:24px}
.page--back{left:620px;background:linear-gradient(135deg,#fbf1ec 0%,#fff 45%,#fbf3ef 100%)}
.page-label{position:absolute;top:1015px;width:556px;text-align:center;font-size:46px;color:#111}
.page-label--front{left:24px}
.page-label--back{left:620px}

.team-photo{position:absolute;left:0;top:0;width:556px;height:231px;background:linear-gradient(120deg,#8a7a66 0%,#c9b9a2 45%,#6b5a48 100%)}

.wordmark{position:absolute;display:flex;align-items:center;gap:8px;font-family:'Cinzel',serif;font-weight:400;color:var(--red);letter-spacing:1px}
.wordmark__mark{width:26px;height:26px;border:1.5px solid #9a9a9a}
.page--front .wordmark{left:148px;top:254px;font-size:34px}
.page--back .wordmark{right:22px;top:22px;font-size:30px}

.tagline-band{position:absolute;left:0;top:314px;width:556px;height:87px}
.tagline{position:absolute;top:345px;left:118px;display:flex;align-items:center;gap:12px;font-family:'Cinzel',serif}
.tagline__lead{color:var(--red);font-size:22px;font-weight:600;border-bottom:2px solid var(--red);line-height:1}
.tagline__box{border:1.5px solid var(--red);background:#fff;padding:5px 10px;font-size:21px;color:var(--grey);letter-spacing:1px}

.content{position:absolute;left:22px;right:22px}
.page--front .content{top:417px}
.page--back .content{top:318px;left:29px;right:28px}
.section-title{font-family:'Cinzel',serif;font-size:11.5px;color:var(--red);font-weight:600;border-bottom:1px solid var(--red);display:inline-block;margin-bottom:10px}
.content p{font-size:7.2px;line-height:1.38;margin-bottom:7px}
.point{display:flex;align-items:center;gap:7px;font-size:9.6px;font-weight:700;color:#333;margin:8px 0 4px}
.point::before{content:"";width:8px;height:8px;border:2px solid var(--red);border-radius:50%;flex:none}
.content p.tight{margin-bottom:2px}
.related{font-family:'Cinzel',serif;font-size:8.4px;font-weight:600;margin:6px 0 3px;color:#333}
.page--back .point{margin:6px 0 3px}
.page--back .related{margin:4px 0 2px}
.page--back .section-title{margin-bottom:8px}

.service-visual{position:absolute;left:26px;top:70px;width:530px;height:239px}

.social{position:absolute;top:682px;left:334px;display:flex;gap:20px;font-size:7.2px}
.social__item{display:flex;align-items:center;gap:6px}
.social__dot{width:18px;height:18px;background:var(--red);border-radius:50%}
.social__sq{width:17px;height:17px;background:var(--red)}
.divider{position:absolute;left:0;top:703px;width:300px;height:6px;background:var(--grey-light)}

.footer{position:absolute;left:0;width:556px;height:44px}
.page--front .footer{top:722px}
.page--back .footer{top:718px}
.footer__text{position:absolute;top:0;left:0;height:44px;color:#fff;font-size:8.6px;display:grid;grid-template-columns:160px 220px;row-gap:6px;padding:7px 0 0 24px}
.page--back .footer__text{grid-template-columns:158px 260px}
.footer__item{display:flex;align-items:flex-start;gap:8px}
.footer__item svg{flex:none;margin-top:1px}
.footer__addr{font-size:7.4px;line-height:1.2}
</style>
</head>
<body>

<section class="page page--front">
  <div class="team-photo" role="img" aria-label="Photo of a diverse team of five smiling colleagues in a bright office"></div>

  <div class="wordmark"><span class="wordmark__mark"></span>LumoByte</div>

  <svg class="tagline-band" viewBox="0 0 556 87" aria-hidden="true">
    <rect x="60" y="0" width="496" height="87" fill="#dcdcdc"/>
    <polygon points="0,17 55,17 0,92" fill="#6e6e70"/>
    <polygon points="20,87 92,0 125,0 53,87" fill="var(--red)"/>
    <polygon points="92,0 125,0 110,18 82,12" fill="var(--red-dark)"/>
  </svg>
  <div class="tagline">
    <span class="tagline__lead">Innovate</span>
    <span class="tagline__box">At the Speed of NOW</span>
  </div>

  <div class="content">
    <h2 class="section-title">About Us</h2>
    <p>LumoByte is an Executive Information Technology Consulting Firm. We specialize in combining people with technology to deliver the Business of IT. We partner with C-Level Executives and their organizations to leverage technology that drives innovation and accelerates business transformation and enable businesses, governments and educational institutions to operate more successfully in a world where everything is increasingly linked together.</p>
    <p>From workshops to full IT assessments, from technology installations and upgrades to major architecture design and implementation, our unique approach, depth and breadth of offerings, and exceptional team help organizations everywhere understand how their IT services can be optimized and leveraged to their strategic advantage.</p>
    <div class="point">The LUMOBYTE Advantage</div>
    <p class="tight">LumoByte is well-known and respected for our innovation and for putting our clients first. We are committed to four essential values</p>
    <div class="point">Leading with perspective as your trusted advisor</div>
    <p class="tight">we move the industry forward with our unique insights, points of view, ideas and solutions, leading our clients, partners and each other to think beyond the ordinary.</p>
    <div class="point">Delivering real impact as your solver</div>
    <p class="tight">We dig hard into your problem and evaluate the bigger picture, then unite the optimal people, technology and know-how to execute the most effective solution.</p>
    <div class="point">Working in the trenches as your partner</div>
    <p class="tight">we work shoulder to shoulder with you, understanding your needs as a team member, and acting in the belief that your success is ours.</p>
    <div class="point">Unlocking tomorrow as your innovator</div>
    <p class="tight">we are relentlessly focused on fostering up great strategies, architecting great solutions, and designing for innovation by allowing our clients to see their IT challenges through a different lens.<br>At LumoByte, our mission is to become your trusted advisor.</p>
  </div>

  <div class="footer">
    <svg width="556" height="44" viewBox="0 0 556 44" aria-hidden="true">
      <polygon points="0,0 450,0 470,44 0,44" fill="var(--red)"/>
      <polygon points="450,0 478,0 505,44 477,44" fill="#5d5d5f"/>
      <polygon points="490,6 512,6 532,40 510,40" fill="var(--red)"/>
    </svg>
    <div class="footer__text">
      <div class="footer__item"><svg width="9" height="9" viewBox="0 0 10 10"><path d="M2 0.5 L4 3 L3 4.2 Q4.5 6.2 5.8 7 L7 5.9 L9.5 8 L8.3 9.5 Q3.5 9 0.5 1.7Z" fill="#fff"/></svg>(555) 014-2290</div>
      <div class="footer__item"><svg width="10" height="8" viewBox="0 0 10 8"><rect x="0.5" y="0.5" width="9" height="7" fill="none" stroke="#fff"/><path d="M0.5 0.5 L5 4.5 L9.5 0.5" fill="none" stroke="#fff"/></svg>READYTOINNOVATE@LUMOBYTE.COM</div>
      <div class="footer__item"><svg width="9" height="9" viewBox="0 0 10 10"><circle cx="5" cy="5" r="4.3" fill="none" stroke="#fff"/><ellipse cx="5" cy="5" rx="1.8" ry="4.3" fill="none" stroke="#fff"/><path d="M0.7 5H9.3" stroke="#fff"/></svg>WWW.LUMOBYTE.COM</div>
      <div class="footer__item footer__addr"><svg width="8" height="10" viewBox="0 0 8 10"><path d="M4 10 L1 5 A3.3 3.3 0 1 1 7 5Z" fill="#fff"/><circle cx="4" cy="3.6" r="1.2" fill="var(--red)"/></svg><span>LAKEVIEW, NY (HEADQUARTERS)<br>210 HARBOR SQUARE, SUITE 900 LAKEVIEW, NY 14000</span></div>
    </div>
  </div>
</section>

<section class="page page--back">
  <div class="wordmark"><span class="wordmark__mark"></span>LumoByte</div>

  <svg class="service-visual" viewBox="0 0 530 239">
    <defs>
      <linearGradient id="cityTone" x1="0" y1="0" x2="1" y2="1">
        <stop offset="0" stop-color="#7fc6e6"/>
        <stop offset="0.5" stop-color="#2a6f9c"/>
        <stop offset="1" stop-color="#0f2f4d"/>
      </linearGradient>
    </defs>
    <polygon role="img" aria-label="Image of a businessman with digital network and security icons over a city skyline" points="50,0 530,0 530,239 200,239" fill="url(#cityTone)"/>
    <polygon points="0,6 38,6 207,239 165,239" fill="var(--red)"/>
  </svg>

  <div class="content">
    <h2 class="section-title">Our Services</h2>
    <p>LumoByte's passion for the Business of IT and our commitment to quality results means we focus on the right solutions to meet your specific needs. Our focus on understanding, quantifying and measuring business results is a unique differentiator that allows us to deliver high-value, high-touch solutions with proven ROI. Our suite of services includes:</p>
    <div class="point">Solutions-as-a-Service</div>
    <p class="tight">We provide end-to-end solutions, utilizing consulting methodologies that are refined by decades of experience, across multiple disciplines. Whether you are addressing network, compute, data protection, virtualization or security, we provide the resources and expertise that allow your company to reach its goals.</p>
    <div class="point">Related Services</div>
    <p class="tight">Data Center Infrastructure, Data Center Facility Selection, Design and Build, Data Center Migration, Business Continuity and Disaster Recovery, Converged Infrastructure, Collaboration &amp; Mobility, External Infrastructure Strategy &amp; Selection.</p>
    <div class="point">C-Suite-as-a-Service</div>
    <p class="tight">We let you run your business while we help you plan, develop, evaluate, manage &amp; co-ordinate technology centric solutions</p>
    <div class="related">Related Services</div>
    <p class="tight">Strategy Assessments, Executive Advising, CTO/CIO On Demand, Virtual CTO/CIO</p>
    <div class="point">Technology Business Management (TBM)-as-a-Service</div>
    <p class="tight">We help clients navigate the changing landscape at the intersection of Business and Technology enabling them to improve the way they make technology decisions. This allows them to optimize costs, quality and the overall value of their IT services</p>
    <div class="related">Related Services:</div>
    <p class="tight">Cloud Migration Programs, Cloud Strategy Roadmap Planning, Data Center &amp; Vendor Consolidation, Application Rationalization, Infrastructure Technology Assessment, IT Organization Change Management, IT Budget and Forecasting Process, Infrastructure Cost Savings Assessment</p>
    <div class="point">Managed Security Services</div>
    <p class="tight">Let us serve as a remote extension of your team to strengthen your security response and defenses.</p>
    <div class="related">Related Services:</div>
    <p class="tight">Security Intelligence Including Co-Managed On-Premise SIEM, Hosted Multi-Tenant SIEM, Use Case Development and Best Practices, Monitoring and Notification, Log Management, Event Archiving, Platform, Vulnerability and Endpoint Management, Malware Remediation</p>
  </div>

  <div class="social">
    <div class="social__item"><span class="social__dot"></span>LUMOBYTE</div>
    <div class="social__item"><span class="social__sq"></span>@LUMOBYTE</div>
  </div>
  <div class="divider"></div>

  <div class="footer">
    <svg width="556" height="44" viewBox="0 0 556 44" aria-hidden="true">
      <polygon points="0,0 430,0 452,44 0,44" fill="var(--red)"/>
      <polygon points="438,0 466,0 492,44 464,44" fill="#5d5d5f"/>
      <polygon points="476,6 498,6 520,40 498,40" fill="var(--red)"/>
    </svg>
    <div class="footer__text">
      <div class="footer__item"><svg width="9" height="9" viewBox="0 0 10 10"><path d="M2 0.5 L4 3 L3 4.2 Q4.5 6.2 5.8 7 L7 5.9 L9.5 8 L8.3 9.5 Q3.5 9 0.5 1.7Z" fill="#fff"/></svg>(555) 014-2290</div>
      <div class="footer__item"><svg width="10" height="8" viewBox="0 0 10 8"><rect x="0.5" y="0.5" width="9" height="7" fill="none" stroke="#fff"/><path d="M0.5 0.5 L5 4.5 L9.5 0.5" fill="none" stroke="#fff"/></svg>READYTOINNOVATE@LUMOBYTE.COM</div>
      <div class="footer__item"><svg width="9" height="9" viewBox="0 0 10 10"><circle cx="5" cy="5" r="4.3" fill="none" stroke="#fff"/><ellipse cx="5" cy="5" rx="1.8" ry="4.3" fill="none" stroke="#fff"/><path d="M0.7 5H9.3" stroke="#fff"/></svg>WWW.LUMOBYTE.COM</div>
      <div class="footer__item footer__addr"><svg width="8" height="10" viewBox="0 0 8 10"><path d="M4 10 L1 5 A3.3 3.3 0 1 1 7 5Z" fill="#fff"/><circle cx="4" cy="3.6" r="1.2" fill="var(--red)"/></svg><span>LAKEVIEW, NY (HEADQUARTERS)<br>210 HARBOR SQUARE, SUITE 900 LAKEVIEW, NY 14000</span></div>
    </div>
  </div>
</section>

<div class="page-label page-label--front">front</div>
<div class="page-label page-label--back">back</div>

</body>
</html>
```